Business Card for a Dental Office

The design should communicate integrity, quality and reliability. We also want the card look elegant, simple, but still stand out, different from the traditional-dental-office business card.

Business

```html
<!DOCTYPE html>
<html lang="en">
<head>
<meta charset="utf-8">
<title>Harbour Lane Dental – Business Card</title>
<link href="https://fonts.googleapis.com/css2?family=Bebas+Neue&family=Source+Sans+3:wght@400;600;700&display=swap" rel="stylesheet">
<style>
  :root{
    --ink:#111111;
    --paper:#ffffff;
    --gold:#c9b21c;
    --gold-deep:#a8931a;
    --gold-bright:#f3e51c;
    --tagline:#b39a1e;
    --stage:#e9e6e1;
  }
  *{margin:0;padding:0;box-sizing:border-box}
  html,body{width:1200px;height:1000px;overflow:hidden}
  body{background:var(--stage);position:relative;font-family:"Source Sans 3",Arial,sans-serif;color:var(--ink)}

  .card{position:absolute;left:265px;width:666px;height:398px;background:var(--paper);box-shadow:0 4px 14px rgba(0,0,0,.18);overflow:hidden}
  .card--front{top:73px}
  .card--back{top:532px}

  .brand{position:absolute;display:flex;align-items:center}
  .brand__square{background:linear-gradient(135deg,var(--gold-deep),var(--gold-bright));flex:none}
  .brand__text{display:flex;flex-direction:column}
  .brand__name{font-family:"Bebas Neue",Impact,sans-serif;color:var(--ink);line-height:.9;letter-spacing:.5px;white-space:nowrap}
  .brand__tagline{color:var(--tagline);text-transform:uppercase;letter-spacing:1.5px;font-weight:400;white-space:nowrap}

  .card--front .brand{left:33px;top:70px}
  .card--front .brand__square{width:60px;height:60px;margin-right:16px}
  .card--front .brand__name{font-size:40px}
  .card--front .brand__tagline{font-size:14.5px;margin-top:2px}

  .card--back .brand{left:97px;top:150px}
  .card--back .brand__square{width:84px;height:84px;margin-right:20px}
  .card--back .brand__name{font-size:46px}
  .card--back .brand__tagline{font-size:16.5px;margin-top:2px}

  .person{position:absolute;right:32px;top:203px;text-align:right}
  .person__name{font-size:21px;font-weight:700;line-height:1}
  .person__role{font-size:16px;margin-top:9px;line-height:1}
  .person__tab{position:absolute;right:0;top:206px;width:13px;height:39px;background:var(--gold)}
  .rule{position:absolute;left:33px;top:242px;width:520px;height:1.5px;background:var(--ink)}

  .address{position:absolute;left:33px;top:297px;font-size:16px;line-height:24px;font-style:normal}
  .contacts{position:absolute;right:32px;top:275px;list-style:none;font-size:16px;line-height:23px;text-align:right}
  .contacts li{display:flex;justify-content:flex-end;align-items:center}
  .contacts svg{width:15px;height:12px;margin-left:9px;fill:var(--gold)}

  .band{position:absolute;left:0;bottom:0;width:100%;height:33px;
    background:linear-gradient(90deg,var(--ink) 0%,var(--ink) 52%,var(--gold-deep) 52%,var(--gold) 70%,var(--gold-bright) 100%)}
</style>
</head>
<body>

<section class="card card--front" aria-label="Business card front">
  <div class="brand">
    <span class="brand__square"></span>
    <div class="brand__text">
      <span class="brand__name">Harbour Lane Dental</span>
      <span class="brand__tagline">Caring for every smile, every day</span>
    </div>
  </div>

  <div class="person">
    <p class="person__name">Owen Reid, PHA</p>
    <p class="person__role">President</p>
  </div>
  <span class="person__tab"></span>
  <span class="rule"></span>

  <address class="address">
    Level 12, 48 Kent Street<br>
    Sydney, New South Wales
  </address>

  <ul class="contacts">
    <li>+ 000 000 0000
      <svg viewBox="0 0 16 12" aria-label="Phone"><path d="M1 4c0-2 3-3 7-3s7 1 7 3v1.5h-3.5V4H4.5v1.5H1z M3.5 6.5h9L14 11H2z"/></svg>
    </li>
    <li>+ 000 000 0000
      <svg viewBox="0 0 16 12" aria-label="Fax"><path d="M4 0h8v3H4z M1 4h14v5h-3V7H4v2H1z M4.5 8h7v4h-7z"/></svg>
    </li>
    <li>info@harbourlanedental.com
      <svg viewBox="0 0 16 12" aria-label="Email"><path d="M0 0h16v1.5L8 7 0 1.5z M0 3.5l8 5.5 8-5.5V12H0z"/></svg>
    </li>
  </ul>

  <div class="band"></div>
</section>

<section class="card card--back" aria-label="Business card back">
  <div class="brand">
    <span class="brand__square"></span>
    <div class="brand__text">
      <span class="brand__name">Harbour Lane Dental</span>
      <span class="brand__tagline">Caring for every smile, every day</span>
    </div>
  </div>
</section>

</body>
</html>
```